Plume Ovenworks, need a business card design for an innovative bakery

This is a new company out of Boston. We develop innovative baking products. I would you to make a simple card with the colors attached. The design should be modern and fun. Our tag line is " The sweetest way to gift". This should be incorporated into the design.

Industry/Entity Type

Business

Contact Information for Business Card

Plume Ovenworks LLC

Font styles to use
Sans Serif

Requirements
Must have
• Felix Marrow
• Address: 818 Tindle Ave, Suite 2190, Newton MA, 02466
• Phone: 617-5930268
• Emial: FelixMarrow@plumeovenworks.example

```html
<!DOCTYPE html>
<html lang="en">
<head>
<meta charset="utf-8">
<title>Plume Ovenworks LLC — Business Card</title>
<link rel="stylesheet" href="https://fonts.googleapis.com/css2?family=Libre+Franklin:wght@600&family=Arimo:ital@1&family=Archivo+Narrow&display=swap">
<style>
  :root {
    --backdrop: #3a120d;
    --card: #a9736d;
    --navy: #1b2a40;
    --teal: #7fd0cc;
    --ink: #1d2a3d;
  }
  html, body {
    margin: 0;
    width: 1200px;
    height: 1000px;
    overflow: hidden;
    background: var(--backdrop);
  }
  .card {
    position: absolute;
    left: 37px;
    top: 127px;
    width: 1125px;
    height: 676px;
    background: var(--card);
    overflow: hidden;
  }
  .card__wave {
    position: absolute;
    left: 0;
    top: 0;
    width: 1125px;
    height: 676px;
  }
  .brand-mark {
    position: absolute;
    left: 77px;
    top: 75px;
    width: 170px;
    height: 170px;
    background: var(--navy);
    display: flex;
    align-items: center;
    justify-content: center;
    text-align: center;
  }
  .brand-mark__name {
    font-family: "Libre Franklin", sans-serif;
    font-weight: 600;
    font-size: 17px;
    line-height: 1.2;
    color: var(--teal);
  }
  .company {
    position: absolute;
    left: 314px;
    top: 92px;
    margin: 0;
    font-family: "Libre Franklin", sans-serif;
    font-weight: 600;
    font-size: 64px;
    line-height: 1;
    letter-spacing: -0.5px;
    color: var(--navy);
    white-space: nowrap;
  }
  .company__accent { color: var(--teal); }
  .tagline {
    position: absolute;
    left: 316px;
    top: 178px;
    margin: 0;
    font-family: "Archivo Narrow", sans-serif;
    font-size: 28px;
    line-height: 1.2;
    color: var(--ink);
    white-space: nowrap;
  }
  .person {
    position: absolute;
    left: 0;
    width: 1196px;
    top: 295px;
    margin: 0;
    text-align: center;
    font-family: "Arimo", sans-serif;
    font-style: italic;
    font-weight: 400;
    font-size: 46px;
    color: var(--ink);
  }
  .contact {
    position: absolute;
    top: 466px;
    font-family: "Archivo Narrow", sans-serif;
    font-size: 29px;
    line-height: 40px;
    color: var(--ink);
    text-align: center;
    white-space: nowrap;
  }
  .contact--address { left: 238px; transform: translateX(-50%); }
  .contact--phone { left: 542px; transform: translateX(-50%); }
  .contact--email { left: 870px; transform: translateX(-50%); }
  .contact p { margin: 0; }
</style>
</head>
<body>
  <section class="card">
    <svg class="card__wave" viewBox="0 0 1125 676" role="img" aria-label="Decorative fine-line teal wave pattern sweeping across the top-left corner">
      <defs>
        <linearGradient id="waveTone" x1="0" y1="0" x2="1" y2="1">
          <stop offset="0" stop-color="#8fc9c6" stop-opacity="0.55"/>
          <stop offset="1" stop-color="#8fc9c6" stop-opacity="0.3"/>
        </linearGradient>
      </defs>
      <path d="M0 0 H578 C545 190 430 340 220 420 C110 465 35 515 0 553 Z" fill="url(#waveTone)"/>
    </svg>

    <div class="brand-mark">
      <span class="brand-mark__name">Plume<br>Ovenworks</span>
    </div>

    <h1 class="company"><span class="company__accent">Plume</span> Ovenworks LLC</h1>
    <p class="tagline">The sweetest way to gift</p>

    <h2 class="person">Felix Marrow</h2>

    <div class="contact contact--address">
      <p>Address:</p>
      <p>818 Tindle Ave, Suite 2190,</p>
      <p>Newton MA, 02466</p>
    </div>
    <div class="contact contact--phone">
      <p>Phone:</p>
      <p>617-5930268</p>
    </div>
    <div class="contact contact--email">
      <p>Emial:</p>
      <p>FelixMarrow@plumeovenworks.example</p>
    </div>
  </section>
</body>
</html>
```